Bright Paddock Learning Program with the aim of promoting a skills football to school aged children to

Need an A5 back to front one page brochure which is colourful, fun and active to attract the students to purchase the football with part of the funds going back to the school.
Whole idea is to get more footballs in the hands of children of primary school age, fo the school to earn funds from the sale as well as us also making some funds from the sale.
Target Market(s)
5-11 Year old boys and girls
Industry/Entity Type
School
Colors
219ed3
ffffff
0255a3
33b8a4
ec1f27
Requirements
Must have
- Must have football, price, promotional words as per example and contact details of who is ordering the footballs.
- Have included a version we have done up but are not happy with, needs to be much more professional than the attachment to the brief.
Nice to have
- Promotional component on the front with plenty of colours and attraction, with detail requirements on the back
Should not have
- No soccer or KRB balls, only Aussie Rules Footballs in design

```html
<!DOCTYPE html>
<html lang="en">
<head>
<meta charset="utf-8">
<title>Footies for Schools – Bright Paddock Learning Program</title>
<link rel="stylesheet" href="https://fonts.googleapis.com/css2?family=Anton&family=Oswald:wght@500;700&family=PT+Sans:wght@400;700&family=Nunito:wght@800&family=Libre+Baskerville&display=swap">
<style>
:root{
  --backdrop:#44494c;
  --sky:#a9e4f6;
  --sky-light:#d6f3fb;
  --grass:#3d9a2b;
  --grass-dark:#2c7d1f;
  --lime:#9be21e;
  --red:#ec1f27;
  --blue:#1f3ed6;
  --navy:#0255a3;
  --cyan:#219ed3;
  --teal:#33b8a4;
  --mint:#5ee6a5;
  --white:#ffffff;
}
*{box-sizing:border-box;margin:0;padding:0}
html,body{width:1200px;height:1019px;overflow:hidden;background:var(--backdrop)}
.sheet{position:absolute;top:115px;width:561px;height:795px;overflow:hidden;background:linear-gradient(var(--sky) 0%,var(--sky-light) 100%)}
.sheet--front{left:27px}
.sheet--back{left:613px}
.sheet svg.ground{position:absolute;inset:0}
.abs{position:absolute}

/* front */
.hero-photo{position:absolute;left:21px;top:29px;width:520px;height:520px;border-radius:50%;border:5px solid var(--white);
  background:radial-gradient(circle at 50% 35%,#cfe9f8 0%,#9fd2ef 35%,#6aa84a 62%,#3f8e2a 100%)}
.price-badge{left:21px;top:21px;width:152px;height:152px;border-radius:50%;background:var(--red);border:6px solid var(--white);
  box-shadow:0 2px 6px rgba(0,0,0,.3);color:var(--white);font-family:'Anton',sans-serif;text-align:center;transform:rotate(6deg);line-height:1}
.price-badge .just{font-size:24px;margin-top:20px}
.price-badge .amount{font-size:58px;letter-spacing:-1px}
.price-badge .each{font-size:26px}
.brand{right:24px;top:26px;width:180px;text-align:center;font-family:'Libre Baskerville',serif;color:var(--blue);font-size:10px;line-height:1.3}
.brand .dot{display:block;width:34px;height:34px;border-radius:50%;background:var(--blue);margin:0 auto 8px}
.bubble-order{left:358px;top:323px;width:206px;height:92px;background:var(--blue);border:3px solid var(--white);border-radius:46px;
  transform:rotate(13deg);color:var(--white);font-family:'Anton',sans-serif;font-size:12.5px;line-height:1.3;text-align:center;padding-top:16px;letter-spacing:.3px}
.bubble-miss{left:13px;top:483px;width:180px;height:70px;background:var(--mint);border:3px solid var(--white);border-radius:14px;
  color:var(--white);font-family:'Anton',sans-serif;font-size:22px;line-height:1.05;text-align:center;padding-top:10px;transform:rotate(-2deg)}
.headline{right:32px;font-family:'Anton',sans-serif;color:var(--red);text-shadow:2px 3px 0 #7a0a0e,0 0 6px rgba(0,0,0,.35);line-height:1}
.headline--top{top:478px;font-size:60px;letter-spacing:1px}
.headline--bottom{top:556px;font-size:80px;letter-spacing:1px}
.pitch{left:0;width:561px;top:656px;text-align:center;font-family:'Oswald',sans-serif;font-weight:700;color:var(--blue);font-size:11px;line-height:1.55;letter-spacing:.6px;text-transform:uppercase}
.reg{left:137px;top:743px;display:flex;height:23px;font-family:'Nunito',sans-serif;font-weight:800;font-size:11px;color:var(--white);letter-spacing:.4px}
.reg span{display:flex;align-items:center;padding:0 15px;white-space:nowrap}
.reg .reg-label{background:var(--blue);border-radius:5px 0 0 5px;width:139px}
.reg .reg-url{background:var(--mint);border-radius:0 5px 5px 0;width:150px}

/* back */
.order{left:23px;top:19px;width:512px;height:131px;background:var(--white);border:3px solid var(--blue);padding:9px 18px 6px;
  font-family:'Oswald',sans-serif;font-weight:700;color:var(--blue);font-size:8.5px;line-height:12px}
.order h2{font-size:11px;line-height:13px;margin-bottom:8px}
.order .row{display:flex;align-items:flex-end;height:12px;margin-bottom:8px;gap:4px;white-space:nowrap}
.order .line{flex:1;border-bottom:1px solid var(--blue);height:10px}
.order .box{width:11px;height:11px;border:1px solid var(--blue);margin:0 5px 0 12px}
.order .office{font-size:9px;height:12px;margin-bottom:4px}
.order .row--last{width:62%;margin-bottom:0}
.fine{left:27px;top:153px;font-family:'Oswald',sans-serif;font-size:5px;color:var(--blue);font-weight:700}
.about-title{left:36px;top:198px;font-family:'PT Sans',sans-serif;font-size:25px;color:#10220c}
.about-text{left:36px;top:231px;width:470px;font-family:'PT Sans',sans-serif;font-size:8px;line-height:1.28;color:var(--white)}
.about-text p{margin-bottom:9px}
.about-text p.narrow{width:340px}
.brand--back{right:38px;top:232px;width:150px;color:var(--white)}
.brand--back .dot{background:var(--white)}
.contacts{left:26px;top:648px;width:520px;font-family:'PT Sans',sans-serif;font-size:9.5px;color:#1a1a1a;line-height:1.12}
.contacts .col{position:absolute;top:0;white-space:nowrap}
.contacts h3{font-weight:400;font-size:10px;margin-bottom:9px}
</style>
</head>
<body>

<section class="sheet sheet--front">
  <svg class="ground" viewBox="0 0 561 795" aria-hidden="true">
    <polygon points="0,165 561,121 561,557 0,605" fill="var(--grass)"/>
    <line x1="0" y1="170" x2="561" y2="126" stroke="var(--lime)" stroke-width="8"/>
    <line x1="330" y1="139" x2="561" y2="118" stroke="var(--white)" stroke-width="9" stroke-dasharray="12 10"/>
    <line x1="330" y1="139" x2="561" y2="118" stroke="var(--grass-dark)" stroke-width="9" stroke-dasharray="10 12" stroke-dashoffset="10"/>
    <line x1="0" y1="598" x2="561" y2="550" stroke="var(--lime)" stroke-width="8"/>
    <line x1="0" y1="610" x2="561" y2="562" stroke="var(--white)" stroke-width="10" stroke-dasharray="14 10"/>
    <line x1="0" y1="610" x2="561" y2="562" stroke="var(--grass-dark)" stroke-width="10" stroke-dasharray="10 14" stroke-dashoffset="12"/>
  </svg>

  <div class="hero-photo" role="img" aria-label="Photo of children in red and black jerseys running to kick a yellow Aussie Rules football on a school oval"></div>

  <div class="abs price-badge">
    <div class="just">JUST</div>
    <div class="amount">$17</div>
    <div class="each">eACh</div>
  </div>

  <div class="abs brand">
    <span class="dot"></span>
    COASTAL JUNIOR FOOTBALL LEAGUE
  </div>

  <div class="abs bubble-order">ORDER YOUR OWN<br>EXCLUSIVE 12" SKILL FOOTBALL<br>IN YOUR LOCAL CSFL CLUB COLOURS</div>

  <div class="abs bubble-miss">DON'T MISS OUT<br>ON A FOOTY!</div>

  <h1 class="abs headline headline--top">FOOTIES FOR</h1>
  <div class="abs headline headline--bottom">SCHOOLS</div>

  <p class="abs pitch">Improve your technique this season and help fundraise money for your school.<br>All orders delivered in term 2 just in time for footy season.<br>$5 from each football purchased will go straight<br>back to your schools P&amp;C!</p>

  <div class="abs reg"><span class="reg-label">Online Registration</span><span class="reg-url">kidsfooty.org/join</span></div>
</section>

<section class="sheet sheet--back">
  <svg class="ground" viewBox="0 0 561 795" aria-hidden="true">
    <polygon points="0,185 561,125 561,557 0,613" fill="var(--grass)"/>
    <line x1="0" y1="190" x2="561" y2="130" stroke="var(--lime)" stroke-width="8"/>
    <line x1="0" y1="180" x2="561" y2="120" stroke="var(--white)" stroke-width="8" stroke-dasharray="12 10"/>
    <line x1="0" y1="180" x2="561" y2="120" stroke="var(--grass-dark)" stroke-width="8" stroke-dasharray="10 12" stroke-dashoffset="10"/>
    <line x1="0" y1="606" x2="561" y2="550" stroke="var(--lime)" stroke-width="8"/>
    <line x1="0" y1="618" x2="561" y2="562" stroke="var(--white)" stroke-width="10" stroke-dasharray="14 10"/>
    <line x1="0" y1="618" x2="561" y2="562" stroke="var(--grass-dark)" stroke-width="10" stroke-dasharray="10 14" stroke-dashoffset="12"/>
  </svg>

  <div class="abs order">
    <h2>ORDER INFORMATION</h2>
    <div class="row">Student Name :<span class="line"></span></div>
    <div class="row">Year:<span class="line" style="flex:.35"></span>Classroom :<span class="line"></span>Number of footballs:<span class="line" style="flex:.3"></span></div>
    <div class="row">Payment method :<span class="box"></span>Cash<span class="box"></span>Cheque<span class="box"></span>EFT</div>
    <div class="office">OFFICE ONLY</div>
    <div class="row row--last">Payment received:<span class="line"></span></div>
  </div>
  <div class="abs fine">*OFFER ONLY AVAILABLE AT SELECTED SCHOOLS</div>

  <h2 class="abs about-title">About Us</h2>
  <div class="abs brand brand--back">
    <span class="dot"></span>
    COASTAL JUNIOR FOOTBALL LEAGUE
  </div>
  <div class="abs about-text">
    <p class="narrow">The Coastal Junior Football League (CJFL) is the caretaker of football throughout the State and is responsible for the overall development of the game.</p>
    <p class="narrow">The CJFL's role includes ownership of the State's two senior teams – the Harbour Kestrels and Riverside Football Club, guiding the Coastal State Football League (CSFL), overseeing community football, managing umpiring, and driving participation through game development and the talent pathway.</p>
    <p>The CJFL is a not for profit sports association. It is incorporated under the Associations Incorporation Act and governed by a voluntary Board of Commissioners that oversees the operation of all football activities throughout the State. The CJFL features more than 100 employees spread across the State.</p>
    <p>The CJFL plays an important role in funding the ongoing development of football via our affiliates, schools, competitions and academies across all WA communities. This ensures that football is the best resourced sporting code in the State and can have the most active role in building better communities through various development programs.</p>
    <p>The rich history of football in the community of Western Australia stretches back to 1885. Today it is the most popular sporting code in the state with 105,000 club participants, of which from Kickstart to Seniors, 7% identify as Aboriginal and Torres Strait Islander.</p>
    <p>This results in a significant social benefit and the creation of better communities through the active promotion of the sport and its associated values of teamwork, responsibility, respect, leadership, commitment and community participation.</p>
    <p>While many of these benefits have long been the result of our activities, the Coastal Junior Football League has both harnessed and harvested those activities delivering these benefits, and used the understanding to develop the most comprehensive community benefits programs in Australia.</p>
  </div>

  <div class="abs contacts">
    <div class="col" style="left:0">
      <h3>Reception</h3>
      Phone:&nbsp;&nbsp; +61 8 9000 4821<br>Email:&nbsp;&nbsp;&nbsp; reception@cjfl.org.au
    </div>
    <div class="col" style="left:200px">
      <h3>Address</h3>
      Gate 3 Parkview Oval<br>Meadow Road<br>Eastvale WA 6010<br><br>Office open 8:30am to 5:30pm, Monday to Friday
    </div>
    <div class="col" style="left:432px">
      <h3>Postal Address</h3>
      PO Box 418<br>Eastvale WA 6912
    </div>
  </div>

  <div class="abs reg"><span class="reg-label">Online Registration</span><span class="reg-url">kidsfooty.org/join</span></div>
</section>

</body>
</html>
```